Propose new minimalist design or Improve aesthetics of current one

Looking to create a minimalist clean business card, you can create your own concept using the elements we already have or improve on that one. Signature does not have to be used if a better idea is proposed.

Target Market(s)

Millennials, minimalist

Industry/Entity Type

REAL ESTATE

Contact Information for Business Card

Keep business card details

Colors

Designer to choose only greyscale colors for use in the design.

Requirements
Must have
• Keep business card details
Nice to have
• I like very minimalist fonts, nothing too busy
Should not have
• Curve designs or lines, colorful names, tacky home outlines

```html
<!DOCTYPE html>
<html lang="en">
<head>
<meta charset="utf-8">
<title>Lena Vargas – Business Card</title>
<link href="https://fonts.googleapis.com/css2?family=Montserrat:wght@300;400;700&family=Libre+Baskerville&display=swap" rel="stylesheet">
<style>
  :root {
    --canvas: #c8c8c8;
    --paper: #f4f4f4;
    --ink: #1f1f1f;
    --ink-soft: #4a4a4a;
    --rule: #9a9a9a;
    --night: #141414;
    --night-soft: #262626;
    --white: #f2f2f2;
  }
  * { margin: 0; padding: 0; box-sizing: border-box; }
  html, body { width: 1200px; height: 1069px; overflow: hidden; }
  body {
    background: var(--canvas);
    font-family: "Montserrat", sans-serif;
    position: relative;
  }
  .card {
    position: absolute;
    left: 250px;
    width: 700px;
    height: 400px;
    box-shadow: 0 10px 28px rgba(0,0,0,.18);
  }
  /* front */
  .card--front { top: 90px; background: var(--paper); color: var(--ink); }
  .agent-name {
    position: absolute; left: 52px; top: 56px;
    font-size: 50px; line-height: .95; letter-spacing: 1px;
  }
  .agent-name__first { display: block; font-weight: 700; }
  .agent-name__last { display: block; font-weight: 300; }
  .agent-title {
    position: absolute; left: 56px; top: 170px;
    font-size: 13px; letter-spacing: 2px; color: var(--ink-soft);
  }
  .brand {
    position: absolute; right: 48px; top: 52px;
    display: flex; align-items: center; gap: 12px;
  }
  .brand__mark { width: 14px; height: 14px; background: var(--ink); }
  .brand__name { font-size: 16px; font-weight: 400; letter-spacing: 1px; }
  .brand-tagline {
    position: absolute; right: 48px; top: 84px; text-align: right;
    font-size: 10px; letter-spacing: 3px; color: var(--ink-soft);
  }
  .brand-tagline__rule { display: block; width: 90px; height: 1px; background: var(--rule); margin: 6px 0 6px auto; }
  .contact-list {
    position: absolute; left: 52px; bottom: 50px; list-style: none;
    font-family: "Libre Baskerville", serif; font-size: 15px;
  }
  .contact-list li { display: flex; align-items: center; gap: 14px; margin-top: 12px; }
  .contact-icon {
    width: 26px; height: 26px; border-radius: 50%; background: var(--ink);
    display: flex; align-items: center; justify-content: center;
  }
  .office-address {
    position: absolute; right: 48px; bottom: 56px; text-align: right;
    font-family: "Libre Baskerville", serif; font-size: 15px; line-height: 1.7;
    font-style: normal;
  }
  /* back */
  .card--back { top: 560px; background: linear-gradient(160deg, var(--night-soft), var(--night)); color: var(--white); overflow: hidden; }
  .portrait {
    position: absolute; left: 60px; bottom: 0; width: 300px; height: 330px;
    background: radial-gradient(ellipse at 50% 40%, #6b5a50 0%, #3a302b 45%, #141414 80%);
  }
  .motto {
    position: absolute; right: 52px; top: 120px;
    font-size: 22px; font-weight: 300; letter-spacing: 3px;
  }
  .signature {
    position: absolute; right: 90px; top: 190px; width: 180px; height: 60px;
    background: linear-gradient(90deg, rgba(255,255,255,.08), rgba(255,255,255,.16));
  }
  .back-title {
    position: absolute; right: 90px; top: 262px;
    font-size: 13px; font-weight: 700; letter-spacing: 2px;
  }
</style>
</head>
<body>
  <section class="card card--front">
    <h1 class="agent-name">
      <span class="agent-name__first">LENA</span>
      <span class="agent-name__last">VARGAS</span>
    </h1>
    <p class="agent-title">REALTOR</p>

    <div class="brand">
      <span class="brand__mark"></span>
      <span class="brand__name">Bright Door Homes</span>
    </div>
    <p class="brand-tagline">Moving Families<span class="brand-tagline__rule"></span>Forward</p>

    <ul class="contact-list">
      <li>
        <span class="contact-icon">
          <svg width="12" height="14" viewBox="0 0 12 14"><rect x="2" y="1" width="8" height="12" rx="1.5" fill="none" stroke="#f4f4f4" stroke-width="1.4"/><circle cx="6" cy="10.5" r=".9" fill="#f4f4f4"/></svg>
        </span>
        555.014.2290
      </li>
      <li>
        <span class="contact-icon">
          <svg width="14" height="10" viewBox="0 0 14 10"><rect x=".7" y=".7" width="12.6" height="8.6" fill="none" stroke="#f4f4f4" stroke-width="1.2"/><path d="M1 1l6 5 6-5" fill="none" stroke="#f4f4f4" stroke-width="1.2"/></svg>
        </span>
        lena@brightdoorhomes.com
      </li>
      <li>
        <span class="contact-icon">
          <svg width="12" height="12" viewBox="0 0 12 12"><circle cx="6" cy="6" r="4.5" fill="none" stroke="#f4f4f4" stroke-width="1.3"/></svg>
        </span>
        @lenavargasrealty
      </li>
    </ul>

    <address class="office-address">1420 West Palo Verde Road,<br>Suite 210, Mesa, AZ 85201</address>
  </section>

  <section class="card card--back">
    <div class="portrait" role="img" aria-label="Portrait photograph of the realtor on a dark background"></div>
    <p class="motto">MOVING YOU FORWARD...</p>
    <div class="signature" role="img" aria-label="Handwritten signature of Lena Vargas"></div>
    <p class="back-title">REALTOR®</p>
  </section>
</body>
</html>
```